Zielgruppe
Wir beraten Menschen aus unterschiedlichen Branchen, die im Rahmen Ihrer Tätigkeit vor einem technologischen Problem bzw. einer technologischen Lücke stehen und helfen diesen über vielfältige Bausteine, um so dem Unternehmen ein Unternehmensupgrade zu verschaffen. Wir schlagen somit eine Brücke zwischen dem Stand von heute in einem Unternehmen zu einem besseren Stand morgen.
Konkret betreiben wir unter anderem externes Projektmanagement, beschaffen Informationen unterschiedlicher Art, vermitteln Kooperationspartner, beraten individuell uvm.
Ob jemand nach einer neuen, innovativen Technologie sucht, Partner benötigt, um eigene Neuentwicklungen voranzutreiben, ein neues Produkt fürs eigene Unternehmen und einen entsprechenden Prototypen sucht, verwendete Stoffe mit anderen ersetzen will - mithilfe unseres weltweiten Expertennetzwerks von über 600.000 direkten Ansprechpartnern finden wir für die meisten Nöte dieser Art eine Lösung bzw. jemanden, der diese lösen kann.
Im Grunde genommen beseitigen wir Engpässe innerhalb von Industrieunternehmen, die beispielsweise sein können
-fehlende TEchnologien/Ersatzprodukte/Ersatzstoffe
-fehlende Ideen für Neuentwicklungen
-fehlendes Wissen im Unternehmen
-fehlende Objektivität hinsichtlich interner Verbesserungsmöglichkeiten
-fehlende Zeit für eigene Projekte, Neuentwicklungen und Suchen versch. Art
Wir finden
- neue Technologien, Ersatzprodukte, Ersatzstoffe
- Ideen für Neuentwicklungen und zusätzlich diejenigen, die dabei unterstützen können
- neue Märkte, um das Unternehmen zu erweitern
- das fehlende Wissen
- den nötigen Abstand, um interne Prozesse und Abläufe objektiv zu beurteilen und geben Vorschläge zur Veränderung/Verbesserung
- passende Realisierungspartner
Wie?
- wir recherchieren (Patente, Literatur) und sammeln Hintergrundwissen
- wir befragen unser Netzwerk und Unternehmen/Wissenschaftler
- wir setzen unsere Töchter..
Aufgabenstellung
Wir benötigen einen faltbaren Flyer, allerdings keinen klassischen, sondern wie ein Theatervorhang. Beispielbilder sind anbei (wir würden die Flyer drucken lassen und dann selbst falten). Wir gehen gerne andere Wege, auch in unseren Projekten.
Der Mensch und dessen Wünsche soll im Mittelpunkt stehen.
Design sollte nicht zu verspielt sein, sich daran orientieren, dass deutsche Unternehmen damit angesprochen werden.
Einen Beispielflyer mit den (noch variablen) Texten ist beigefügt, das Design muss sich nicht daran orientieren. Gute Alternativen sind mehr als gewünscht.
Der Gedanke hinter dem Flyer: Wir schlagen eine Brücke für den Kunden/Menschen zu seinem Ziel. Die Tools, die wir dazu nutzen sind Steine oder wir sprengen den Weg frei zum Ziel o.ä. Auch hier sind Alternativen mehr als willkommen.
Sie dürfen sich so weit wie möglich vom Beispielentwurf und dem Bild der Brücke zum Ziel lösen. Je kreativer und einleuchtender, desto besser. Gerne auch humorvoll, gerne einfach anders.

```html
<!DOCTYPE html>
<html lang="de">
<head>
<meta charset="utf-8">
<title>vtc Flyer</title>
<link href="https://fonts.googleapis.com/css2?family=Lato:wght@300;400;700;900&display=swap" rel="stylesheet">
<style>
:root{
  --bg:#dfe0e3;
  --paper:#ececee;
  --navy:#2f3b8f;
  --blue:#3a48a3;
  --blue-box:rgba(52,64,160,.88);
  --ink:#2c3785;
  --grey:#6b6f80;
  --white:#ffffff;
}
*{margin:0;padding:0;box-sizing:border-box}
html,body{width:1200px;height:1200px;overflow:hidden;background:var(--bg);font-family:'Lato',sans-serif;color:var(--ink)}
.sheet{position:absolute;left:205px;width:776px;overflow:hidden}
.sheet--outer{top:31px;height:552px}
.sheet--inner{top:615px;height:546px;background:linear-gradient(180deg,#e6e8ee 0%,#d9dce4 60%,#d3d6dd 100%)}
.nowrap{white-space:nowrap}

/* outer side */
.panel-photo{position:absolute;top:0;bottom:0}
.panel-photo--left{left:0;width:193px;background:linear-gradient(180deg,#2f6fc2 0%,#5a9ad8 45%,#4a5f8a 70%,#9fb0c8 100%)}
.panel-photo--right{left:583px;width:193px;background:linear-gradient(180deg,#5d88c9 0%,#3f5d92 40%,#28385a 70%,#8a9ab8 100%)}
.panel-center{position:absolute;left:193px;top:0;width:390px;height:100%;background:var(--paper)}
.team-photo{position:absolute;left:0;top:182px;width:390px;height:205px;background:linear-gradient(135deg,#e8e4df 0%,#b9b2aa 40%,#6f6a72 70%,#3d4260 100%)}
.blue-box{position:absolute;background:var(--blue-box);color:var(--white)}
.engpass{left:35px;top:334px;width:141px;bottom:0;padding:19px 0 0 12px;font-weight:300;font-size:17px;line-height:21px;white-space:nowrap}
.engpass b,.problem b{font-weight:700}
.problem{left:600px;top:0;width:140px;height:386px;padding:18px 0 0 10px;white-space:nowrap}
.problem h2{font-weight:300;font-size:17px;line-height:21px}
.problem .sorge{font-weight:900;font-size:17.4px;margin-top:8px}
.problem .lead{font-size:9px;font-weight:300;margin-top:3px}
.problem .lead b{font-weight:700;font-style:italic}
.checks{list-style:none;margin-top:12px}
.checks li{position:relative;padding-left:20px;font-size:9px;font-weight:300;line-height:11px;margin-bottom:6.5px}
.checks svg{position:absolute;left:0;top:2px}

.brand{position:absolute;display:flex;align-items:center;gap:6px;font-weight:400;font-size:22px;color:var(--blue);letter-spacing:.5px}
.brand .dot{width:22px;height:22px;border-radius:50%;background:var(--blue)}
.headline{position:absolute;left:51px;font-weight:300;font-size:17.4px;line-height:21px;color:var(--ink);white-space:nowrap}
.contact{position:absolute;left:51px;top:462px;width:292px;font-size:9px;color:var(--ink);white-space:nowrap}
.contact .name{font-weight:700}
.contact .role,.contact .line{font-weight:300;color:var(--grey)}
.contact .firm{font-weight:700;margin-top:8px}
.contact .right{position:absolute;right:0;top:25px;text-align:right}
.line{display:flex;align-items:center;gap:5px;line-height:11.5px}
.contact .right .line{justify-content:flex-end}

/* inner side */
.backdrop{position:absolute;inset:0;background:linear-gradient(180deg,rgba(255,255,255,0) 0%,rgba(150,158,180,.25) 45%,rgba(150,158,180,.15) 65%,rgba(255,255,255,0) 100%)}
.fold{position:absolute;top:0;bottom:0;width:1px;background:rgba(255,255,255,.6)}
.band{position:absolute;left:0;right:0;top:86px;height:77px;background:var(--navy)}
.band p{position:absolute;left:233px;top:7px;color:var(--white);font-weight:300;font-size:17.4px;line-height:21px;white-space:nowrap}
.band b{font-weight:700}
.band .brandword{font-style:italic}
.stuck{position:absolute;left:15px;top:187px;font-weight:300;font-size:17.4px;line-height:21px;white-space:nowrap}
.stuck b{font-weight:700}
.quote{position:absolute;background:var(--navy);color:var(--white);font-weight:700;font-size:16.5px;line-height:20px;padding:1px 7px;white-space:nowrap}
.tools .vline{position:absolute;top:189px;width:1px;height:232px;background:var(--ink)}
.tool{position:absolute;font-size:9px;line-height:11px;font-weight:300;color:var(--ink);white-space:nowrap}
.tool b{font-weight:700}
.icon{position:absolute;width:16px;height:16px}
.upgrade{position:absolute;left:272px;top:463px;font-weight:300;font-size:17.4px;line-height:21px;white-space:nowrap}
.upgrade b{font-weight:700}
.arrow{position:absolute;left:0;top:477px}
.solve{position:absolute;left:596px;top:187px;font-weight:300;font-size:17.4px;line-height:21px;white-space:nowrap}
.solve b{font-weight:700}
.rocket-art{position:absolute;left:627px;top:306px;width:102px;height:112px;background:linear-gradient(180deg,#3a48a3 0%,#5b5f73 100%);border-radius:40px 40px 6px 6px;opacity:.85}
</style>
</head>
<body>

<section class="sheet sheet--outer">
  <div class="panel-photo panel-photo--left" role="img" aria-label="Foto einer Hängebrücke vor blauem Himmel über Wasser"></div>
  <div class="blue-box engpass">Wir beseitigen<br>Ihre <b>Engpässe</b><br>und sind Ihnen<br>ein strategischer<br><b>Partner</b> von<br>Beginn bis zum<br>Ende Ihres<br>Projekts.</div>

  <div class="panel-center">
    <div class="brand" style="left:262px;top:22px"><span class="dot"></span>vtc</div>
    <p class="headline" style="top:112px">Sie nennen mir Ihre Ziele und Wünsche.<br>Gemeinsam definieren wir Ihr Projekt.</p>
    <div class="team-photo" role="img" aria-label="Foto eines Teams, das gemeinsam an einem Bildschirm arbeitet"></div>
    <p class="headline" style="top:415px">Nutzen Sie unser Expertennetzwerk.</p>
    <div class="contact">
      <div class="name">Dr. Lukas Brenner</div>
      <div class="role">Geschäftsführender Gesellschafter</div>
      <div class="firm">Vantec Innovationsberatung GmbH</div>
      <div class="line"><svg width="8" height="8" viewBox="0 0 8 8"><path d="M1 1v6M1 1h5l-1 2 1 2H1" fill="none" stroke="#2c3785" stroke-width="1"/></svg>Lindenallee 12</div>
      <div class="line"><svg width="8" height="8" viewBox="0 0 8 8"><path d="M4 1 0.5 4H2v3h4V4h1.5z" fill="#2c3785"/></svg>80331 Musterstadt</div>
      <div class="right">
        <div class="line"><svg width="8" height="8" viewBox="0 0 8 8"><rect x="1" y="3" width="6" height="4" rx="1" fill="#2c3785"/><path d="M0.5 3.5Q4 0 7.5 3.5" fill="none" stroke="#2c3785"/></svg>+49 123 456 78 90</div>
        <div class="line"><svg width="8" height="8" viewBox="0 0 8 8"><rect x="0.5" y="1.5" width="7" height="5" fill="none" stroke="#2c3785"/><path d="M0.5 1.5 4 4.5 7.5 1.5" fill="none" stroke="#2c3785"/></svg>brenner@vantec-beratung.de</div>
        <div class="line"><svg width="8" height="8" viewBox="0 0 8 8"><circle cx="4" cy="4" r="3.5" fill="#2c3785"/></svg>www.vantec-beratung.de</div>
      </div>
    </div>
  </div>

  <div class="panel-photo panel-photo--right" role="img" aria-label="Foto von Brückenpfeilern über ruhigem Wasser"></div>
  <div class="blue-box problem">
    <h2>Sie stehen<br>vor einem<br>technologischen<br>Problem?</h2>
    <div class="sorge">Keine Sorge.</div>
    <div class="lead"><b>vtc</b> bietet mir:</div>
    <ul class="checks">
      <li><svg width="8" height="7" viewBox="0 0 8 7"><path d="M0.5 3.5 3 6 7.5 1" fill="none" stroke="#fff" stroke-width="1.6"/></svg>...neue Technologien,<br>Ersatzprodukte/<br>Ersatzstoffe</li>
      <li><svg width="8" height="7" viewBox="0 0 8 7"><path d="M0.5 3.5 3 6 7.5 1" fill="none" stroke="#fff" stroke-width="1.6"/></svg>...Ideen für<br>Neuentwicklungen</li>
      <li><svg width="8" height="7" viewBox="0 0 8 7"><path d="M0.5 3.5 3 6 7.5 1" fill="none" stroke="#fff" stroke-width="1.6"/></svg>...Zugang zu neuen<br>Märkten</li>
      <li><svg width="8" height="7" viewBox="0 0 8 7"><path d="M0.5 3.5 3 6 7.5 1" fill="none" stroke="#fff" stroke-width="1.6"/></svg>...ergänzendes Wissen</li>
      <li><svg width="8" height="7" viewBox="0 0 8 7"><path d="M0.5 3.5 3 6 7.5 1" fill="none" stroke="#fff" stroke-width="1.6"/></svg>...interne Prozess- und<br>Ablaufverbesserungen</li>
      <li><svg width="8" height="7" viewBox="0 0 8 7"><path d="M0.5 3.5 3 6 7.5 1" fill="none" stroke="#fff" stroke-width="1.6"/></svg>...passende Partner<br>zur Realisierung</li>
      <li><svg width="8" height="7" viewBox="0 0 8 7"><path d="M0.5 3.5 3 6 7.5 1" fill="none" stroke="#fff" stroke-width="1.6"/></svg>...ein Expertennetzwerk<br>von über 600.000<br>Ansprechpartnern</li>
    </ul>
  </div>
</section>

<section class="sheet sheet--inner">
  <div class="backdrop" role="img" aria-label="Blasses Foto einer Brücke über Wasser als Hintergrund"></div>
  <div class="fold" style="left:196px"></div>
  <div class="fold" style="left:581px"></div>
  <div class="brand" style="left:672px;top:16px"><span class="dot"></span>vtc</div>

  <div class="band"><p><b class="brandword">vtc</b> übernimmt die <b>Gesamtprojektleitung</b><br>als Generalunternehmer und nutzt für Ihr<br>Projekt eigene, passende Tools:</p></div>

  <p class="stuck">Sie stecken im Projekt<br>fest und kommen nicht<br>weiter? Wir helfen<br>Ihnen <b>schnell</b>, einfach<br>und <b>unkompliziert</b>.</p>
  <div class="quote" style="left:18px;top:330px">“Geht nicht,</div>
  <div class="quote" style="left:73px;top:351px">gibt´s nicht.”</div>

  <div class="tools">
    <div class="vline" style="left:265px"></div>
    <div class="vline" style="left:427px"></div>

    <svg class="icon" style="left:236px;top:192px" viewBox="0 0 16 16"><circle cx="8" cy="4" r="3" fill="#666"/><circle cx="3" cy="11" r="2" fill="#666"/><circle cx="8" cy="11" r="2" fill="#666"/><circle cx="13" cy="11" r="2" fill="#666"/></svg>
    <p class="tool" style="left:272px;top:190px">Heterogenes Team mit<br><b>kreativen Köpfen</b></p>
    <svg class="icon" style="left:400px;top:192px" viewBox="0 0 16 16"><rect x="1" y="2" width="14" height="12" rx="1" fill="#666"/><path d="M3 6h10M3 9h10M3 12h10" stroke="#fff"/></svg>
    <p class="tool" style="left:435px;top:189px"><b>Patent- und</b><br><b>Literatur</b>recherchen</p>

    <svg class="icon" style="left:236px;top:243px" viewBox="0 0 16 16"><rect x="3" y="1" width="10" height="14" fill="#666"/><path d="M5 4h6M5 7h6M5 10h6" stroke="#fff"/></svg>
    <p class="tool" style="left:272px;top:229px">Tochterunternehmen für<br>Spezialthemen;<br><b>Werkstattrat,</b><br><b>Forma9, Lumen Labs</b></p>
    <svg class="icon" style="left:400px;top:243px" viewBox="0 0 16 16"><rect x="2" y="2" width="12" height="9" fill="#666"/><path d="M8 11v4" stroke="#666" stroke-width="2"/></svg>
    <p class="tool" style="left:435px;top:230px">Geographisch spezifische<br>Projektausschreibungen<br>und <b>Netzwerkbefragungen</b></p>

    <svg class="icon" style="left:236px;top:298px" viewBox="0 0 16 16"><circle cx="6" cy="8" r="5" fill="none" stroke="#666" stroke-width="1.5"/><rect x="12" y="2" width="3" height="12" fill="#666"/></svg>
    <p class="tool" style="left:272px;top:296px"><b>Globales Netzwerk</b> in jedem<br>Technologiebereich</p>
    <svg class="icon" style="left:400px;top:296px" viewBox="0 0 16 16"><circle cx="8" cy="7" r="5" fill="#666"/><rect x="6" y="12" width="4" height="3" fill="#666"/></svg>
    <p class="tool" style="left:435px;top:296px">Individuelles<br><b>Projektmanagement</b></p>

    <svg class="icon" style="left:236px;top:346px" viewBox="0 0 16 16"><rect x="2" y="1" width="12" height="14" rx="1" fill="#666"/><circle cx="8" cy="8" r="3" fill="none" stroke="#fff"/></svg>
    <p class="tool" style="left:273px;top:345px">Demonstrator- und<br><b>Prototypenbau</b></p>
    <svg class="icon" style="left:400px;top:346px" viewBox="0 0 16 16"><rect x="2" y="1" width="12" height="14" rx="1" fill="#666"/><path d="M5 11 11 5" stroke="#fff" stroke-width="1.5"/></svg>
    <p class="tool" style="left:437px;top:345px">Tests, Sprint,<br><b>Validierung</b></p>

    <svg class="icon" style="left:236px;top:397px" viewBox="0 0 16 16"><rect x="1" y="1" width="6" height="5" fill="#666"/><rect x="9" y="10" width="6" height="5" fill="#666"/><path d="M4 6v6h5" fill="none" stroke="#666" stroke-width="1.5"/></svg>
    <p class="tool" style="left:273px;top:391px">Dokumentation und<br><b>Visualisierung</b> über<br>Web-Plattform NOVIS</p>
    <svg class="icon" style="left:400px;top:398px" viewBox="0 0 16 16"><rect x="2" y="1" width="12" height="14" rx="1" fill="#666"/><path d="M5 12V9M8 12V6M11 12V8" stroke="#fff" stroke-width="1.5"/></svg>
    <p class="tool" style="left:437px;top:398px">Professionelle <b>Marktanalyse</b><br>und Technologieauswertung</p>
  </div>

  <svg class="arrow" width="250" height="10" viewBox="0 0 250 10"><path d="M0 5.5H240" stroke="#2f3b8f" stroke-width="1.2"/><path d="M240 1 249 5 240 9z" fill="#2f3b8f"/></svg>
  <p class="upgrade"><b>Unternehmensupgrade</b> durch<br>technologische Beratung</p>

  <p class="solve">Wir <b>lösen</b> Ihre<br>unternehmerischen<br><b>Probleme</b> durch unser<br>Wissen und unsere<br>Tools.</p>
  <div class="rocket-art" role="img" aria-label="Illustration von drei startbereiten Raketen"></div>
</section>

</body>
</html>
```